Pediatric Dental Practice needs a postcard for direct mail advertising

We are looking for a creative and professional double-sided postcard design for a direct mail marketing campaign. Our goal is to attract new families to our pediatric dental practice by conveying a sense of warmth, modern care, and clinical excellence. The design should feel "boutique" and high-end yet remain fun and approachable for parents and children.

```html
<!DOCTYPE html>
<html lang="en">
<head>
<meta charset="utf-8">
<title>Birchwood Pediatric Dentistry – Postcard Design</title>
<link href="https://fonts.googleapis.com/css2?family=Lexend:wght@300;400;500;600&family=Kalam:wght@700&display=swap" rel="stylesheet">
<style>
  :root{
    --green:#3f9b52;
    --green-band:#47a056;
    --green-mid:#7dbb6f;
    --green-light:#d5ebcd;
    --orange:#f7901e;
    --charcoal:#333638;
    --ink:#2f3133;
    --grey:#5b5e60;
    --paper:#fbfaf5;
    --white:#ffffff;
  }
  *{margin:0;padding:0;box-sizing:border-box}
  html,body{width:1200px;height:933px;overflow:hidden;background:var(--white)}
  body{position:relative;font-family:"Lexend",sans-serif;color:var(--ink)}
  .abs{position:absolute}

  /* Presentation header */
  .brand-name{left:54px;top:130px;color:var(--ink);font-weight:400;white-space:nowrap}
  .brand-name .line1{display:block;font-size:40px;line-height:44px;letter-spacing:.5px}
  .brand-name .line2{display:block;font-size:12.5px;letter-spacing:5.2px;margin-top:6px}
  .brand-mark{left:124px;top:44px;width:82px;height:82px;border-radius:50%;background:var(--green-mid)}
  .divider{left:326px;top:69px;width:1px;height:126px;background:#d7d7d7}
  .concept-title{left:359px;top:66px;font-size:25px;font-weight:500;color:var(--green)}
  .concept-sub{left:360px;top:102px;font-size:21px;font-weight:400;color:var(--ink)}
  .concept-desc{left:361px;top:152px;font-size:15px;font-weight:300;line-height:26px;color:var(--grey);width:560px}
  .swatch{top:65px;width:38px;height:38px;border-radius:50%}
  .sw1{left:928px;background:var(--green)}
  .sw2{left:982px;background:var(--green-mid)}
  .sw3{left:1036px;background:var(--green-light)}
  .sw4{left:1091px;background:var(--orange)}
  .sw5{left:1145px;background:var(--charcoal)}
  .side-tag{top:236px;height:23px;border-radius:4px;background:var(--green);color:var(--white);font-size:13px;line-height:23px;text-align:center;font-weight:400}
  .tag-front{left:251px;width:65px}
  .tag-back{left:830px;width:61px}

  /* Cards */
  .card{top:266px;height:602px;background:var(--paper);box-shadow:0 1px 5px rgba(0,0,0,.18);overflow:hidden}
  .card-front{left:28px;width:557px}
  .card-back{left:609px;width:558px}
  .card svg.art{position:absolute;left:0;top:0}

  /* Front */
  .front-mark{left:42px;top:30px;width:44px;height:44px;border-radius:50%;background:var(--green-mid)}
  .front-name{left:29px;top:84px;color:var(--ink);font-weight:400;white-space:nowrap}
  .front-name .line1{display:block;font-size:22px;line-height:24px}
  .front-name .line2{display:block;font-size:7.5px;letter-spacing:2.9px;margin-top:2px}
  .headline{left:28px;top:142px;font-size:33px;line-height:39px;font-weight:500;color:var(--ink)}
  .headline .accent{color:var(--green)}
  .intro{left:29px;top:338px;font-size:11.3px;line-height:18px;font-weight:300;color:var(--ink);width:190px}
  .cta{left:247px;top:527px;color:var(--white)}
  .cta .ask{font-size:15.5px;font-weight:300;display:block}
  .cta .url{font-size:14.5px;font-weight:500;display:block;margin-top:8px}

  /* Back */
  .back-head{left:28px;top:40px;font-size:20px;line-height:26px;font-weight:500;color:var(--ink)}
  .back-head .accent{color:var(--green)}
  .back-intro{left:28px;top:125px;font-size:10.4px;line-height:16.5px;font-weight:300;color:var(--ink);width:190px}
  .indicia{left:453px;top:37px;width:79px;height:88px;border:1.3px solid var(--ink);font-size:8.6px;line-height:15px;text-align:center;padding-top:7px;font-weight:300;letter-spacing:-.1px}
  .indicia b{font-weight:500}
  .addressee{left:351px;top:157px;font-size:12px;line-height:20px;font-weight:400}
  .feature{left:94px;width:150px}
  .feature h3{font-size:11px;font-weight:500;color:var(--green);line-height:14px}
  .feature p{font-size:9.2px;font-weight:300;line-height:14.5px;color:var(--ink);margin-top:2px}
  .f1{top:243px}.f2{top:321px}.f3{top:399px}
  .rooted{left:320px;top:316px;width:202px;text-align:center}
  .rooted h3{font-size:14.5px;font-weight:500;line-height:21px;color:var(--green)}
  .rooted p{font-size:10.3px;font-weight:300;line-height:16.5px;margin-top:5px;color:var(--ink)}
  .back-mark{left:74px;top:505px;width:30px;height:30px;border-radius:50%;background:var(--green-mid)}
  .back-name{left:32px;top:545px;color:var(--white);font-weight:400;white-space:nowrap;text-align:center;width:114px}
  .back-name .line1{display:block;font-size:14.5px;line-height:16px}
  .back-name .line2{display:block;font-size:5.6px;letter-spacing:1.9px;margin-top:2px}
  .contact{left:205px;color:var(--white);font-size:11.3px;font-weight:300;line-height:16px}
  .c1{top:494px}.c2{top:536px}.c3{top:563px}
  .welcome{left:395px;top:508px;font-family:"Kalam",cursive;font-weight:700;color:var(--orange);font-size:15px;line-height:19px;transform:rotate(-6deg);text-align:center;width:110px}
</style>
</head>
<body>

<header>
  <div class="abs brand-mark" aria-hidden="true"></div>
  <div class="abs brand-name"><span class="line1">Birchwood</span><span class="line2">PEDIATRIC DENTISTRY</span></div>
  <div class="abs divider"></div>
  <h1 class="abs concept-title">Creative Idea: The Birchwood Smile Path</h1>
  <h2 class="abs concept-sub" style="font-weight:400">Postcard Design</h2>
  <p class="abs concept-desc">A graceful, flowing design inspired by the birch tree and a child’s smile—guiding families to a warm, friendly dental home.</p>
  <span class="abs swatch sw1"></span><span class="abs swatch sw2"></span><span class="abs swatch sw3"></span><span class="abs swatch sw4"></span><span class="abs swatch sw5"></span>
  <span class="abs side-tag tag-front">FRONT</span>
  <span class="abs side-tag tag-back">BACK</span>
</header>

<!-- Front side -->
<section class="abs card card-front">
  <svg class="art" width="557" height="602" viewBox="0 0 557 602">
    <defs>
      <linearGradient id="roomTone" x1="0" y1="0" x2="1" y2="1">
        <stop offset="0" stop-color="#ece6c8"/>
        <stop offset=".45" stop-color="#cfd6ac"/>
        <stop offset=".75" stop-color="#55aaa5"/>
        <stop offset="1" stop-color="#c79a5c"/>
      </linearGradient>
    </defs>
    <path d="M557 -10 L557 450 L290 450 C235 410,215 330,218 250 C221 145,270 50,395 10 C455 -8,520 -10,557 -10 Z" fill="var(--green-light)"/>
    <path role="img" aria-label="Photo of a bright pediatric dental treatment room with a teal exam chair and two small chairs by a window" d="M557 2 L557 440 L300 440 C250 400,230 330,232 250 C234 150,282 62,400 22 C460 4,520 2,557 2 Z" fill="url(#roomTone)"/>
    <path d="M0 482 C120 422,220 394,320 412 C420 430,480 414,557 402 L557 420 C480 432,420 448,320 430 C220 412,120 440,0 500 Z" fill="var(--green-light)"/>
    <path d="M0 492 C120 432,220 404,320 422 C420 440,480 424,557 412 L557 602 L0 602 Z" fill="var(--green-band)"/>
    <path d="M115 512 C175 440,270 418,350 442 C425 466,470 478,484 470" fill="none" stroke="var(--white)" stroke-width="1.3" stroke-dasharray="4 4"/>
    <path d="M488 474 C478 466,472 461,472 455 C472 450,476 447,480 447 C484 447,487 450,488 452 C489 450,492 447,496 447 C500 447,504 450,504 455 C504 461,498 466,488 474 Z" fill="var(--orange)"/>
    <circle cx="85" cy="545" r="35" fill="var(--white)"/>
    <g fill="none" stroke="var(--green)" stroke-width="2.4" stroke-linecap="round" stroke-linejoin="round">
      <rect x="68" y="529" width="34" height="32" rx="4"/>
      <path d="M68 539 H102 M77 524 V533 M93 524 V533 M78 550 L83 555 L92 545"/>
    </g>
    <path d="M44 304 Q84 334 125 304" fill="none" stroke="var(--orange)" stroke-width="3" stroke-linecap="round"/>
    <path d="M40 301 L47 307 M129 301 L122 307" stroke="var(--orange)" stroke-width="3" stroke-linecap="round"/>
  </svg>
  <div class="abs front-mark" aria-hidden="true"></div>
  <div class="abs front-name"><span class="line1">Birchwood</span><span class="line2">PEDIATRIC DENTISTRY</span></div>
  <h2 class="abs headline">A warm<br><span class="accent">dental home</span><br>for growing<br><span class="accent">smiles</span></h2>
  <p class="abs intro">Compassionate care, modern comfort, and a gentle approach to help kids feel confident about their smiles.</p>
  <p class="abs cta"><span class="ask">Schedule your child’s visit today!</span><span class="url">birchwoodkidsdental.com</span></p>
</section>

<!-- Back side -->
<section class="abs card card-back">
  <svg class="art" width="558" height="602" viewBox="0 0 558 602">
    <path d="M278 0 L300 0 C302 70,270 120,238 150 C205 182,160 205,90 210 C40 214,12 222,0 230 L0 480 L232 480 C262 420,276 340,258 282 C242 232,250 190,275 140 C292 105,298 60,278 0 Z" fill="var(--green-light)"/>
    <path d="M312 300 C300 252,380 245,430 250 C510 255,562 282,546 350 C535 410,470 432,420 426 C360 420,326 400,320 362 C316 338,316 320,312 300 Z" fill="var(--green-light)"/>
    <rect role="img" aria-label="Line drawing of a family holding hands" x="393" y="274" width="58" height="42" rx="8" fill="#c3dfba"/>
    <path d="M423 279 C417 275,413 272,413 268 C413 265,416 263,418 263 C421 263,422 265,423 266 C424 265,425 263,428 263 C430 263,433 265,433 268 C433 272,429 275,423 279 Z" fill="var(--orange)"/>
    <path d="M36 276 C10 300,8 322,34 336 M36 354 C10 378,8 400,34 414 M36 432 C20 452,18 466,24 480" fill="none" stroke="var(--white)" stroke-width="1.3" stroke-dasharray="4 4"/>
    <path d="M0 476 C150 470,300 456,420 448 C500 443,540 458,558 470 L558 602 L0 602 Z" fill="var(--charcoal)"/>
    <path d="M37 94 Q64 118 93 94" fill="none" stroke="var(--orange)" stroke-width="2.4" stroke-linecap="round"/>
    <g>
      <circle cx="57" cy="261" r="26" fill="var(--green)"/>
      <circle cx="57" cy="261" r="21" fill="none" stroke="var(--white)" stroke-width="1.2"/>
      <path d="M57 249 L60 257 L68 258 L62 263 L64 271 L57 267 L50 271 L52 263 L46 258 L54 257 Z" fill="none" stroke="var(--white)" stroke-width="1.6" stroke-linejoin="round"/>
      <circle cx="57" cy="339" r="26" fill="var(--green)"/>
      <circle cx="57" cy="339" r="21" fill="none" stroke="var(--white)" stroke-width="1.2"/>
      <path d="M57 328 V350 M46 339 H68 M50 332 L64 346 M64 332 L50 346" stroke="var(--white)" stroke-width="1.6" stroke-linecap="round"/>
      <circle cx="57" cy="417" r="26" fill="var(--green)"/>
      <circle cx="57" cy="417" r="21" fill="none" stroke="var(--white)" stroke-width="1.2"/>
      <path d="M57 404 C66 410,66 424,57 430 C48 424,48 410,57 404 Z M57 410 V432 M57 418 L62 413 M57 423 L52 418" fill="none" stroke="var(--white)" stroke-width="1.6" stroke-linecap="round" stroke-linejoin="round"/>
    </g>
    <g>
      <circle cx="184" cy="502" r="9" fill="var(--green-mid)"/>
      <path d="M184 507 C180 502,179 500,179 498 A5 5 0 0 1 189 498 C189 500,188 502,184 507 Z" fill="var(--white)"/>
      <circle cx="184" cy="498" r="1.6" fill="var(--green-mid)"/>
      <circle cx="184" cy="544" r="9" fill="var(--green-mid)"/>
      <path d="M180 539 L182 538 L184 541 L182.5 542.5 C183.5 544.5,184.5 545.5,186.5 546.5 L188 545 L191 547 L190 549 C185 549,180 544,180 539 Z" fill="var(--white)"/>
      <circle cx="184" cy="571" r="9" fill="var(--green-mid)"/>
      <g fill="none" stroke="var(--white)" stroke-width="1"><circle cx="184" cy="571" r="5"/><ellipse cx="184" cy="571" rx="2.2" ry="5"/><path d="M179 571 H189"/></g>
    </g>
  </svg>
  <h2 class="abs back-head"><span class="accent">Growing smiles.</span><br>Growing confidence.</h2>
  <p class="abs back-intro">At Birchwood Pediatric Dentistry, we make every visit a positive experience for kids and peace of mind for parents.</p>
  <div class="abs indicia">PRSRT STD<br>ECRWSS<br>U.S. POSTAGE<br><b>PAID</b><br>EDDM RETAIL</div>
  <p class="abs addressee">Local<br>Postal Customer</p>
  <div class="abs feature f1"><h3>Kid-Friendly Care</h3><p>Gentle, patient-centered care designed just for kids.</p></div>
  <div class="abs feature f2"><h3>Modern Comfort</h3><p>A clean, welcoming space with the latest technology.</p></div>
  <div class="abs feature f3"><h3>Healthy Habits</h3><p>We empower families with education for lifelong smiles.</p></div>
  <div class="abs rooted"><h3>Rooted in care.<br>Growing together.</h3><p>We’re proud to be part of your family’s smile journey.</p></div>
  <div class="abs back-mark" aria-hidden="true"></div>
  <div class="abs back-name"><span class="line1">Birchwood</span><span class="line2">PEDIATRIC DENTISTRY</span></div>
  <p class="abs contact c1">48 Maple Grove Lane, Suite 200<br>Fairview, SC 29990</p>
  <p class="abs contact c2">(555) 010-0147</p>
  <p class="abs contact c3">birchwoodkidsdental.com</p>
  <p class="abs welcome">New patients<br>always welcome!</p>
</section>

</body>
</html>
```